New Coffee Packaging

Update/refresh/modernize range of 1 kg Coffee packaging

Industry/Entity Type

Hospitalty

Requirements
Must have
• Clean. crisp, eye catching
Nice to have
• Verdano means 'Height' specialty coffee is grown at high altitudes, peaks. mountains

```html
<!DOCTYPE html>
<html lang="en">
<head>
<meta charset="utf-8">
<title>Verdano Coffee Co. — 1kg Range</title>
<link rel="stylesheet" href="https://fonts.googleapis.com/css2?family=Montserrat:wght@600;700&family=Saira+Condensed:wght@400;700&family=Rubik:wght@500;700&display=swap">
<style>
  :root {
    --backdrop: #ede4d9;
    --bag-white: #ffffff;
    --ink: #231f20;
    --supreme: #b68442;
    --organic: #85bd4f;
    --black: #000000;
  }
  * { box-sizing: border-box; margin: 0; padding: 0; }
  html, body { width: 848px; height: 1200px; overflow: hidden; }
  body { background: var(--backdrop); position: relative; }

  .bag {
    position: absolute; top: 396px; width: 267px; height: 524px;
    background: var(--bag-white); color: var(--ink); overflow: hidden;
  }
  .bag--supreme { left: 138px; --accent: var(--supreme); }
  .bag--organic { left: 452px; --accent: var(--organic); }

  .range-tab {
    position: absolute; left: 30px; top: 0; width: 29px; height: 120px;
    background: var(--accent);
    display: flex; align-items: flex-end; justify-content: center;
    padding-bottom: 5px;
  }
  .range-tab__label {
    writing-mode: vertical-rl; transform: rotate(180deg);
    font: 700 13px/1 "Montserrat", sans-serif; letter-spacing: 3.2px;
    color: var(--bag-white); white-space: nowrap;
  }

  .est-seal {
    position: absolute; left: 29px; top: 121px; width: 30px; height: 30px;
    border-radius: 50%; background: var(--bag-white); border: 2px solid var(--ink);
  }
  .roast-badge {
    position: absolute; left: 184px; top: 54px; width: 42px; height: 48px;
    border: 1px solid var(--ink); background: var(--bag-white);
  }

  .brand { position: absolute; left: 0; right: 0; top: 136px; text-align: center; }
  .brand__name {
    font: 700 76px/1 "Saira Condensed", sans-serif; color: var(--ink);
    letter-spacing: 0; white-space: nowrap;
  }
  .brand__sub {
    margin-top: 40px; font: 400 21px/1 "Saira Condensed", sans-serif;
    color: var(--ink); letter-spacing: 5px;
  }

  .cup-notes {
    position: absolute; left: 36px; top: 323px; width: 165px; height: 103px;
    background: var(--accent); color: var(--bag-white);
    padding: 18px 0 0 17px;
    font: 700 7.5px/1.2 "Rubik", sans-serif; text-transform: uppercase;
  }
  .bag--supreme .cup-notes { letter-spacing: 3.4px; }
  .bag--organic .cup-notes { letter-spacing: 1.6px; padding-top: 20px; padding-left: 16px; }
  .cup-notes li { list-style: none; margin-bottom: 6px; }
  .bag--organic .cup-notes li { margin-bottom: 3.5px; }

  .brew-options {
    position: absolute; left: 36px; top: 428px; width: 165px; height: 45px;
    border: 1px solid var(--accent); display: flex; justify-content: center; gap: 7px;
    padding-top: 9px;
  }
  .brew-option { width: 17px; display: flex; flex-direction: column; align-items: center; }
  .brew-option svg { width: 11px; height: 11px; }
  .brew-option__label { font: 700 3.6px/1 "Rubik", sans-serif; margin-top: 1px; color: var(--ink); }
  .brew-option__tick {
    width: 7px; height: 7px; border: 0.6px solid var(--ink); border-radius: 50%; margin-top: 3px;
  }

  .profile-strip {
    position: absolute; left: 201px; top: 323px; width: 38px; height: 150px;
    background: var(--black);
    display: flex; align-items: center; justify-content: center;
  }
  .profile-strip__label {
    writing-mode: vertical-rl; transform: rotate(180deg);
    font: 700 11px/1 "Montserrat", sans-serif; letter-spacing: 2px;
    color: var(--bag-white); white-space: nowrap;
  }

  .net-weight {
    position: absolute; left: 0; width: 280px; top: 486px; text-align: center;
    font: 700 16px/1 "Rubik", sans-serif; color: var(--ink); letter-spacing: -0.3px;
  }
</style>
</head>
<body>

<section class="bag bag--supreme">
  <div class="range-tab"><div class="range-tab__label">SUPREME</div></div>
  <div class="est-seal"></div>
  <div class="roast-badge"></div>
  <div class="brand">
    <div class="brand__name">verdano</div>
    <div class="brand__sub">coffee co.</div>
  </div>
  <ul class="cup-notes">
    <li>Honey</li>
    <li>Stone Fruit</li>
    <li>Toffee</li>
    <li>Medium/High<br>Sweetness</li>
  </ul>
  <div class="brew-options">
    <div class="brew-option"><svg viewBox="0 0 12 12"><path d="M1 3h10L7 9H5z" fill="none" stroke="#231f20" stroke-width="1"/></svg><span class="brew-option__label">Filter</span><span class="brew-option__tick"></span></div>
    <div class="brew-option"><svg viewBox="0 0 12 12"><circle cx="4" cy="2.5" r="1.5" fill="none" stroke="#231f20" stroke-width=".8"/><path d="M3 5h3v3H3zM6 7h5" fill="none" stroke="#231f20" stroke-width=".8"/></svg><span class="brew-option__label">Espresso</span><span class="brew-option__tick"></span></div>
    <div class="brew-option"><svg viewBox="0 0 12 12"><path d="M3 3h6v8H3zM6 1v6M4 1h4M9 5h2v3H9" fill="none" stroke="#231f20" stroke-width=".9"/></svg><span class="brew-option__label">Plunger</span><span class="brew-option__tick"></span></div>
    <div class="brew-option"><svg viewBox="0 0 12 12"><ellipse cx="8" cy="4" rx="2.2" ry="3" fill="#231f20"/><ellipse cx="4" cy="8" rx="3" ry="2.2" fill="#231f20"/></svg><span class="brew-option__label">Beans</span><span class="brew-option__tick"></span></div>
  </div>
  <div class="profile-strip"><div class="profile-strip__label">CUP PROFILE</div></div>
  <div class="net-weight">1kg</div>
</section>

<section class="bag bag--organic">
  <div class="range-tab"><div class="range-tab__label">ORGANIC</div></div>
  <div class="est-seal"></div>
  <div class="roast-badge"></div>
  <div class="brand">
    <div class="brand__name">verdano</div>
    <div class="brand__sub">coffee co.</div>
  </div>
  <ul class="cup-notes">
    <li>Certified Organic<br>Arabica Beans</li>
    <li style="margin-top:6px">Sweet</li>
    <li>Herbal</li>
    <li>Smooth Lingering Finish</li>
  </ul>
  <div class="brew-options">
    <div class="brew-option"><svg viewBox="0 0 12 12"><path d="M1 3h10L7 9H5z" fill="none" stroke="#231f20" stroke-width="1"/></svg><span class="brew-option__label">Filter</span><span class="brew-option__tick"></span></div>
    <div class="brew-option"><svg viewBox="0 0 12 12"><circle cx="4" cy="2.5" r="1.5" fill="none" stroke="#231f20" stroke-width=".8"/><path d="M3 5h3v3H3zM6 7h5" fill="none" stroke="#231f20" stroke-width=".8"/></svg><span class="brew-option__label">Espresso</span><span class="brew-option__tick"></span></div>
    <div class="brew-option"><svg viewBox="0 0 12 12"><path d="M3 3h6v8H3zM6 1v6M4 1h4M9 5h2v3H9" fill="none" stroke="#231f20" stroke-width=".9"/></svg><span class="brew-option__label">Plunger</span><span class="brew-option__tick"></span></div>
    <div class="brew-option"><svg viewBox="0 0 12 12"><ellipse cx="8" cy="4" rx="2.2" ry="3" fill="#231f20"/><ellipse cx="4" cy="8" rx="3" ry="2.2" fill="#231f20"/></svg><span class="brew-option__label">Beans</span><span class="brew-option__tick"></span></div>
  </div>
  <div class="profile-strip"><div class="profile-strip__label">CUP PROFILE</div></div>
  <div class="net-weight">1kg</div>
</section>

</body>
</html>
```